3" Round Business Card for Funeral Home

We need a business card designed for our cremation service. We would like to use a 3" round business card.

The business card will be 2-sided. One side with the logo featured prominently. The back sad will have employee name and contact info.

Templates for printing have been attached to project as well as logo

We like soft colors like the logo. Final design should promote a feeling of trust.

Industry/Entity Type

Funeral

Contact Information for Business Card

Employee Name, Phone number, email, web address

Requirements
Should not have
• any sort of funeral item such as urn, casket, hearse, tombstone

```html
<!DOCTYPE html>
<html lang="en">
<head>
<meta charset="utf-8">
<title>Round Business Card – Quiet Harbor</title>
<link rel="stylesheet" href="https://fonts.googleapis.com/css2?family=Nunito+Sans:wght@400;700;800&display=swap">
<style>
  :root {
    --backdrop: #acacac;
    --paper: #ffffff;
    --teal: #13a79c;
    --plum: #91278e;
    --ink-light: #ffffff;
  }
  * { box-sizing: border-box; margin: 0; padding: 0; }
  html, body {
    width: 1200px;
    height: 900px;
    overflow: hidden;
    background: var(--backdrop);
    font-family: "Nunito Sans", Arial, sans-serif;
  }
  .card {
    position: absolute;
    top: 215px;
    width: 414px;
    height: 414px;
    border-radius: 50%;
    overflow: hidden;
  }
  .card--contact { left: 163px; background: var(--paper); }
  .card--brand { left: 623px; background: var(--teal); }

  .brand-name {
    position: absolute;
    left: 0;
    width: 100%;
    text-align: center;
    font-weight: 400;
    font-size: 40px;
    letter-spacing: 0.5px;
    line-height: 1;
  }
  .card--contact .brand-name { top: 100px; color: var(--teal); }
  .card--brand .brand-name { top: 170px; color: var(--ink-light); font-size: 42px; }

  .name-band {
    position: absolute;
    top: 186px;
    left: 0;
    width: 100%;
    height: 77px;
    background: var(--plum);
    color: var(--ink-light);
    text-align: center;
    padding-top: 12px;
  }
  .person-name { font-weight: 800; font-size: 26px; line-height: 1.1; }
  .person-role { font-weight: 400; font-size: 17px; line-height: 1.3; }

  .contact-area {
    position: absolute;
    top: 263px;
    left: 0;
    width: 100%;
    height: 151px;
    background: var(--teal);
    color: var(--ink-light);
    text-align: center;
    padding-top: 28px;
    font-size: 17px;
    line-height: 24px;
  }
  .contact-area p { margin: 0; }
</style>
</head>
<body>
  <section class="card card--contact" aria-label="Card front: contact details">
    <div class="brand-name">quietHarbor.com</div>
    <div class="name-band">
      <p class="person-name">Daniel Harper</p>
      <p class="person-role">Managing Director</p>
    </div>
    <div class="contact-area">
      <p class="contact-phone">555-2040-318</p>
      <p class="contact-email">hello@quietharbor.com</p>
      <p class="contact-web">www.quietharbor.com</p>
    </div>
  </section>

  <section class="card card--brand" aria-label="Card back: brand side">
    <div class="brand-name">quietHarbor.com</div>
  </section>
</body>
</html>
```